Vivid Tapestry Android app screenshots

I need some screenshot backgrounds that will be used as a background for Vivid Tapestry at https://market.qorvalin.net/store/apps/details?id=com.brightpixelworks.tapestry&hl=en-GB . I want to replace that boring orange background with something more exciting, maybe put some icons related to galleries there. Something like https://market.qorvalin.net/store/apps/details?id=com.brightpixelworks.timberline&hl=en-US has been done for the calendar. Let's keep it orange #F57C00 though and the resolution should be 2000x3555, I need 4 slightly different variants. Only the top and the sides of the background will be visible so focus on those parts. I need only the orange backgrounds, not the actual device or screenshot itself.

```html
<!DOCTYPE html>
<html lang="en">
<head>
<meta charset="utf-8">
<title>Vivid Tapestry – Screenshot Background</title>
<link rel="stylesheet" href="https://fonts.googleapis.com/css2?family=Roboto:wght@400&display=swap">
<style>
  :root {
    --orange-base: #ff8200;
    --orange-light: #ff9000;
    --orange-mid: #ff7a00;
    --orange-deep: #ff6d00;
    --orange-deeper: #ff5c00;
    --orange-icon: #ff7600;
    --amber: #ffa000;
    --white: #ffffff;
  }
  html, body {
    margin: 0;
    padding: 0;
    width: 675px;
    height: 1200px;
    overflow: hidden;
    font-family: "Roboto", sans-serif;
  }
  .canvas {
    position: relative;
    width: 675px;
    height: 1200px;
    overflow: hidden;
    background: linear-gradient(90deg, var(--orange-light) 0%, var(--orange-base) 45%, var(--orange-mid) 100%);
  }
  .backdrop {
    position: absolute;
    inset: 0;
    display: block;
  }
</style>
</head>
<body>
<main class="canvas">
  <svg class="backdrop" viewBox="0 0 675 1200" width="675" height="1200" aria-hidden="true">
    <defs>
      <linearGradient id="deep-band" x1="0" y1="0" x2="1" y2="0">
        <stop offset="0" stop-color="#ff6a00"/>
        <stop offset="1" stop-color="#ff5a00"/>
      </linearGradient>
    </defs>

    <!-- light upper wave -->
    <path class="wave-upper" fill="var(--orange-light)"
      d="M0,0 H675 V361 C560,360 470,345 390,300 C250,235 150,120 0,95 Z"/>

    <!-- right sweeping curve -->
    <path class="wave-sweep" fill="var(--orange-mid)" opacity="0.75"
      d="M535,0 H675 V1200 H0 V1150 C120,1000 250,900 420,820 C600,720 655,620 652,500 C650,380 600,230 535,0 Z"/>

    <!-- top-right darker blob -->
    <path class="blob-top" fill="#ff7300"
      d="M390,0 H675 V34 C600,42 520,38 455,22 Z"/>

    <!-- lower bands -->
    <path class="band-lower" fill="var(--orange-deep)"
      d="M0,1053 C200,980 400,960 560,930 C610,920 645,905 675,887 V1200 H0 Z"/>
    <path class="band-bottom" fill="url(#deep-band)"
      d="M0,1040 C150,1010 300,1000 420,1004 C520,1007 600,1010 675,1008 V1200 H0 Z"/>

    <!-- amber corner -->
    <path class="corner-amber" fill="var(--amber)"
      d="M598,1200 C620,1185 650,1172 675,1164 V1200 Z"/>

    <!-- gallery icon, top right -->
    <g class="gallery-icon" fill="none" stroke="var(--orange-icon)" stroke-width="5.5" stroke-linejoin="round" stroke-linecap="round">
      <rect x="0" y="0" width="430" height="252" rx="20" transform="translate(318,56) rotate(-15.5)"/>
      <polyline points="362,240 428,106 572,201"/>
      <polyline points="543,258 606,138 680,186"/>
      <circle cx="549" cy="85" r="29"/>
    </g>

    <!-- gallery icon, bottom left -->
    <g class="gallery-icon-small" fill="none" stroke="var(--orange-icon)" stroke-width="5.5" stroke-linejoin="round" stroke-linecap="round">
      <path d="M-10,1005 L22,996 C40,991 58,1002 63,1020 L112,1205"/>
      <polyline points="0,1205 21,1163 95,1210"/>
    </g>

    <!-- shutter dot, bottom left -->
    <g class="shutter">
      <circle cx="0" cy="1116" r="34" fill="none" stroke="var(--white)" stroke-width="3.5"/>
      <circle cx="0" cy="1116" r="27" fill="var(--white)"/>
    </g>

    <!-- search icon -->
    <g class="search-icon">
      <circle cx="65" cy="143" r="32.5" fill="none" stroke="var(--white)" stroke-width="3.5"/>
      <line x1="91.5" y1="167.5" x2="115" y2="191" stroke="var(--white)" stroke-width="8" stroke-linecap="round"/>
      <line x1="91.5" y1="167.5" x2="115" y2="191" stroke="var(--orange-base)" stroke-width="3" stroke-linecap="round"/>
    </g>
  </svg>
</main>
</body>
</html>
```